Form By Tammi - Health and Wellness Business Card and Logo

I need a business card design with a logo for my business you can check out at www.formbytammi.com. I want something more original, simplistic, and memorable than the basic logo I have on my site currently. I am a health and wellness coach and I offer mindset coaching and nutrition plans. I like the colour teal and dark grey/black for my theme colours. I emphasize growth, longterm change, and the whole package of "healthy mind, healthy body, healthy life". I had played around the idea of intertwining 3 T's or incorporating growth (leaves etc.) into my design. I want my expertise and experience to show through. In one glance I want people to understand with confidence I can help them accomplish anything they set their minds to. I look forward to seeing what everyone comes up with!

Industry/Entity Type

Health And Wellness

Contact Information for Business Card

Form By Tammi
Tammi Orlund
BSc, Health & Wellness Coach
"Manifest your best"
www.formbytammi.com
formbytammi@quillmail.com
613-472-0916
[Instagram logo] @tammiorlund

Colors
33b8a4
ffffff
333333
000000

Requirements
Must have
• A memorable and unique logo for my business!
Nice to have
• Could have the phrase "Are you unhappy with your body and state of health?" or "It takes the right skills to develop habits in order to create long term change. I can help you get there."

```html
<!DOCTYPE html>
<html lang="en">
<head>
<meta charset="utf-8">
<title>Form By Tammi – Business Card</title>
<link href="https://fonts.googleapis.com/css2?family=Nunito:wght@300;400;700&display=swap" rel="stylesheet">
<style>
  :root {
    --teal: #2eaca8;
    --card-front: #eaf6f6;
    --ink: #111111;
    --white: #ffffff;
    --backdrop: #d9d9db;
  }
  html, body {
    margin: 0;
    padding: 0;
    width: 1200px;
    height: 1000px;
    overflow: hidden;
    background: var(--backdrop);
    font-family: "Nunito", sans-serif;
  }
  .canvas {
    position: relative;
    width: 1200px;
    height: 1000px;
  }
  .card {
    position: absolute;
    left: 278px;
    width: 644px;
    height: 376px;
    overflow: hidden;
  }
  .card--front { top: 107px; background: var(--card-front); }
  .card--back  { top: 516px; background: var(--teal); }

  .card__shapes {
    position: absolute;
    inset: 0;
    width: 644px;
    height: 376px;
  }

  .brand {
    position: absolute;
    left: 38px;
    top: 33px;
    display: flex;
    align-items: center;
    gap: 14px;
  }
  .brand__square {
    width: 124px;
    height: 106px;
    border: 4px solid var(--teal);
    border-radius: 16px;
    box-sizing: border-box;
  }
  .brand__name {
    font-weight: 300;
    font-size: 38px;
    line-height: 40px;
    color: var(--ink);
  }

  .person {
    position: absolute;
    left: 38px;
    top: 190px;
  }
  .person__name {
    margin: 0;
    font-weight: 700;
    font-size: 26px;
    line-height: 32px;
    color: var(--teal);
  }
  .person__title {
    margin: 2px 0 0;
    font-weight: 400;
    font-size: 16px;
    color: var(--ink);
  }

  .website {
    position: absolute;
    left: 37px;
    top: 320px;
    font-size: 15px;
    color: var(--ink);
  }

  .tagline {
    position: absolute;
    left: 442px;
    top: 290px;
    color: var(--white);
  }
  .tagline__lead {
    display: block;
    font-weight: 700;
    font-size: 28px;
    line-height: 32px;
  }
  .tagline__words {
    display: block;
    font-weight: 300;
    font-size: 19px;
    line-height: 22px;
  }

  .back-brand {
    position: absolute;
    inset: 0;
    display: flex;
    align-items: center;
    justify-content: center;
    font-weight: 300;
    font-size: 36px;
    color: var(--white);
  }
</style>
</head>
<body>
<main class="canvas">

  <section class="card card--front" aria-label="Business card front">
    <svg class="card__shapes" viewBox="0 0 644 376" aria-hidden="true">
      <circle cx="700" cy="-100" r="199" fill="var(--teal)"/>
      <circle cx="700" cy="-100" r="205" fill="none" stroke="var(--teal)" stroke-width="2"/>
      <circle cx="690" cy="500" r="360" fill="var(--teal)"/>
      <circle cx="690" cy="500" r="367" fill="none" stroke="var(--teal)" stroke-width="2.5"/>
    </svg>

    <div class="brand">
      <div class="brand__square"></div>
      <div class="brand__name">Form<br>By Tammi</div>
    </div>

    <div class="person">
      <h1 class="person__name">Tammi Orlund</h1>
      <p class="person__title">BSc, Health &amp; Wellness Coach, Trainer</p>
    </div>

    <div class="website">www.formbytammi.com</div>

    <div class="tagline">
      <span class="tagline__lead">healthy</span>
      <span class="tagline__words">mind • body • life</span>
    </div>
  </section>

  <section class="card card--back" aria-label="Business card back">
    <div class="back-brand">Form By Tammi</div>
  </section>

</main>
</body>
</html>
```